Cedarline Coalition Web Presence Design and Relaunch

Take existing web files and "clean up" for a a more presentable web landing pad.
posted presently on a site pad CSS template. at www.cedarlinecoalition.org

The site is clunky and unprofessional looking. Needs to be toned down so the urgency is conveyed, but not via a burning planet image.

Target Market(s)

Non-profit climate adaptation group targeting local government land management agencies, special districts and private landholders of natural resource properties.

Industry/Entity Type

Environment

Coding

Coded - Design and coding required

Number of Pages Required

Font styles to use
Serif
Sans Serif

Requirements
Must have
• Include current logos, aspects if content on current site www.cedarlinecoalition.org
• A regional Pacific Northwest Focus (US & Canada). Content speaking to urgency but respectful of cultural diversity and norms. Sustainability themes. Emphasis on action and implementation.
Nice to have
• link to like minded projects. Appear to future generations. Diversity in thematic areas ecological resiliency, energy, food security and infrastructure.

```html
<!DOCTYPE html>
<html lang="en">
<head>
<meta charset="utf-8">
<title>Cedarline Coalition</title>
<link href="https://fonts.googleapis.com/css2?family=Prata&family=Poppins:wght@300;400;500&family=Oswald:wght@500&display=swap" rel="stylesheet">
<style>
:root{
  --green:#a2c83e;
  --green-dark:#8db52f;
  --blue:#0e8fcf;
  --text:#555a5f;
  --white:#ffffff;
  --light:#f4f6f1;
  --dark:#1d2b3a;
}
*{margin:0;padding:0;box-sizing:border-box}
html,body{width:1200px;height:3901px;overflow:hidden;background:var(--white)}
body{position:relative;font-family:"Poppins",sans-serif;color:var(--text)}
.abs{position:absolute}
.serif{font-family:"Prata",serif}
.social{display:flex;gap:8px}
.social span{width:34px;height:34px;border-radius:50%;display:block}
.s1{background:#3b5998}.s2{background:#d34836}.s3{background:#1da1f2}.s4{background:#c4302b}.s5{background:#f08a24}

/* header */
.brand{font-family:"Prata",serif;color:var(--blue);font-size:22px;line-height:1.1;text-align:center}
.brand small{display:block;color:var(--green);font-family:"Poppins",sans-serif;font-size:11px;letter-spacing:4px}
.nav{display:flex;gap:28px;color:var(--white);font-size:14px;letter-spacing:.3px}
.phone{display:flex;align-items:center;gap:10px;color:var(--white);font-family:"Prata",serif;font-size:19px}
.phone i{width:34px;height:34px;border-radius:50%;background:var(--blue);display:flex;align-items:center;justify-content:center}

/* hero */
.hero-photo{left:0;top:148px;width:1200px;height:529px;background:linear-gradient(160deg,#1f3320 0%,#2f4a2a 40%,#5b6a55 65%,#3d7fc4 85%,#6a7a40 100%)}
.hero-kicker{left:177px;top:525px;color:var(--white);font-style:italic;font-weight:300;font-size:27px}
.hero-title{left:177px;top:555px;color:var(--white);font-family:"Oswald",sans-serif;font-size:48px;line-height:52px;width:420px}
.dots{left:1020px;top:651px;display:flex;gap:8px}
.dots span{width:12px;height:12px;border-radius:50%;background:var(--white)}
.dots span.off{background:transparent;border:2px solid var(--white)}

/* about */
.eyebrow{color:var(--green);font-size:21px}
.h-blue{color:var(--blue);font-size:38px}
.para{font-size:15px;line-height:27px}
.stats{left:153px;top:1072px;width:690px;height:135px;background:var(--white);box-shadow:0 4px 18px rgba(0,0,0,.1);display:flex;align-items:center}
.stat{flex:1;text-align:center;font-size:15px;line-height:22px;border-right:1px solid #e2e2e2;padding:0 10px}
.stat:last-child{border:none}
.stat b{display:block;font-family:"Prata",serif;font-weight:400;color:var(--blue);font-size:30px;line-height:44px}

/* projects */
.section-title{width:1200px;text-align:center;font-size:40px}
.project{width:240px}
.project .icon{width:76px;height:76px;background:var(--green);display:flex;align-items:center;justify-content:center}
.project h3{font-family:"Prata",serif;font-weight:400;color:var(--blue);font-size:20px;margin:28px 0 12px}
.project p{font-size:14.5px;line-height:27px}

/* works */
.work-tag{left:77px;top:1927px;width:338px;height:124px;background:var(--green);color:var(--white);padding:24px 46px;z-index:2}
.work-tag h3{font-family:"Prata",serif;font-weight:400;font-size:36px;line-height:46px}
.work-tag p{font-size:16px}
.work-photo{left:0;top:1992px;width:1200px;height:573px;background:linear-gradient(180deg,#5b83b0 0%,#e7b15e 30%,#9aa866 45%,#3f5c33 60%,#262f5a 80%,#2c3c6a 100%)}
.arrows{left:945px;top:1992px;width:255px;height:76px;background:var(--white);display:flex;gap:10px;padding:3px 0 0 78px}
.arrows span{width:46px;height:46px;border:1.5px solid var(--green);display:flex;align-items:center;justify-content:center}

/* green */
.green-bg{left:0;top:2565px;width:1200px;height:697px;background:linear-gradient(90deg,#eef1ea 0%,#fbfcfa 35%,#fff 60%,#f1f4ee 100%)}
.btn{height:50px;display:flex;align-items:center;justify-content:center;color:var(--white);font-family:"Prata",serif;font-size:17px;letter-spacing:.5px}
.tree-photo{left:658px;top:2735px;width:364px;height:365px;background:linear-gradient(180deg,#4a5158 0%,#8fa2b0 35%,#5f8a3a 60%,#9b7a4a 80%,#6d5335 100%)}
.metric{width:146px;height:146px;background:var(--green);color:var(--white);text-align:center;padding-top:14px}
.metric svg{display:block;margin:0 auto 6px}
.metric b{display:block;font-family:"Prata",serif;font-weight:400;font-size:27px;line-height:30px}
.metric span{font-size:16px}

/* contact */
.contact-bg{left:0;top:3262px;width:1200px;height:456px;background:linear-gradient(120deg,#1b2838 0%,#2c3a4a 50%,#1b2838 100%)}
.contact-line{display:flex;gap:20px;color:#e8ecef;font-size:15px;line-height:27px}
.field{border:1px solid #a0a8b2;border-radius:4px;color:#dfe4e8;font-size:14px;padding:18px 16px}

/* footer */
.footer{left:0;top:3718px;width:1200px;height:183px;background:var(--green)}
.foot-links{color:var(--white);font-size:15px}
</style>
</head>
<body>

<!-- header -->
<div class="abs" style="left:0;top:0;width:1200px;height:148px;background:var(--white)"></div>
<svg class="abs" style="left:0;top:0" width="1200" height="148" viewBox="0 0 1200 148">
  <path d="M0 22 H340 C380 22 380 55 410 55 H1200 V118 H400 C360 118 370 148 320 148 H0 Z" fill="var(--green)"/>
  <path d="M0 22 H330 C372 22 366 140 320 148 H0 Z" fill="var(--white)"/>
</svg>
<div class="abs brand" style="left:70px;top:52px;width:130px">Cedarline<small>COALITION</small></div>
<div class="abs social" style="left:922px;top:10px"><span class="s1"></span><span class="s2"></span><span class="s3"></span><span class="s4"></span><span class="s5"></span></div>
<nav class="abs nav" style="left:589px;top:78px"><span>HOME</span><span>ABOUT US</span><span>PROJECTS</span><span>CONTACT</span></nav>
<div class="abs phone" style="left:962px;top:70px"><i><svg width="18" height="18" viewBox="0 0 24 24"><path d="M6.6 10.8a15 15 0 006.6 6.6l2.2-2.2a1 1 0 011-.25 11.4 11.4 0 003.6.57 1 1 0 011 1V20a1 1 0 01-1 1A17 17 0 013 4a1 1 0 011-1h3.5a1 1 0 011 1c0 1.25.2 2.45.57 3.57a1 1 0 01-.25 1z" fill="#fff"/></svg></i>555 014 2290</div>

<!-- hero -->
<div class="abs hero-photo" role="img" aria-label="Field crew in protective gear and helmets wrapping soil in blue sheeting beside a forest edge"></div>
<svg class="abs" style="left:0;top:440px" width="1200" height="237" viewBox="0 0 1200 237">
  <path d="M0 150 C120 80 250 0 380 20 C520 40 600 160 760 170 C900 180 1050 120 1200 60 V237 H0 Z" fill="var(--green)" opacity=".92"/>
</svg>
<div class="abs hero-kicker">Climate Adaptation</div>
<div class="abs hero-title">Implementing Climate Strategies</div>
<div class="abs dots"><span></span><span class="off"></span><span></span><span></span><span></span></div>

<!-- about -->
<div class="abs eyebrow serif" style="left:145px;top:758px">Cedarline Coalition</div>
<h2 class="abs h-blue serif" style="left:155px;top:790px;font-weight:400">What We Are Doing ?</h2>
<p class="abs para" style="left:152px;top:854px;width:385px">Dedicated to taking action the Cedarline Coalition was created to help bring adaptation strategies to life. Working with local communities we are committed to implementing strategies that will sustain communities throughout the Pacific Northwest for generations to come.</p>
<div class="abs" role="img" aria-label="Cupped hands holding soil with a young green seedling" style="left:695px;top:740px;width:395px;height:500px;background:radial-gradient(circle at 60% 25%,#c9e27a 0%,#6d9a2c 35%,#2f4a1c 75%,#2a2418 100%)"></div>
<div class="abs stats">
  <div class="stat"><b>250+</b>Project<br>Completed</div>
  <div class="stat"><b>300+</b>Donations<br>&nbsp;</div>
  <div class="stat"><b>17+</b>Communities<br>Engaged</div>
  <div class="stat"><b>70+</b>Volunteers<br>&nbsp;</div>
</div>

<!-- featured projects -->
<h2 class="abs section-title serif" style="left:0;top:1318px;font-weight:400"><span style="color:var(--green)">Featured</span> <span style="color:var(--blue)">Projects</span></h2>
<div class="abs project" style="left:77px;top:1424px">
  <div class="icon"><svg width="44" height="44" viewBox="0 0 44 44" fill="none" stroke="#1d2b3a" stroke-width="1.6"><path d="M8 4h20l8 8v28H8z"/><path d="M14 16h14M14 22h14M14 28h8"/><path d="M36 22l-10 12-3 1 1-3 10-12z"/></svg></div>
  <h3>Adaptation Plans</h3><p>Communities throughout the region have adopted plans to to address our changing climate. Many more are in the process of developing plans.</p>
</div>
<div class="abs project" style="left:344px;top:1424px">
  <div class="icon"><svg width="44" height="44" viewBox="0 0 44 44" fill="none" stroke="#1d2b3a" stroke-width="1.6"><path d="M4 32l8-4h10l8 4 8-6"/><path d="M4 38h10l16-4"/><path d="M22 22c0-8 6-14 16-14 0 10-6 14-16 14z"/><path d="M22 22l10-8"/></svg></div>
  <h3>On The ground…</h3><p>The Alliance is familiar and growing throughout the region. Presently our work has us on the ground in keystone watersheds in the Cascade</p>
</div>
<div class="abs project" style="left:610px;top:1424px">
  <div class="icon"><svg width="44" height="44" viewBox="0 0 44 44" fill="none" stroke="#1d2b3a" stroke-width="1.6"><path d="M6 6h26v30H10a4 4 0 01-4-4z"/><path d="M6 12h26"/><circle cx="32" cy="32" r="8" fill="#0e8fcf" stroke="#1d2b3a"/><path d="M32 28v8M29 33l3 3 3-3" stroke="#fff"/></svg></div>
  <h3>Ecological Resilience</h3><p>To endure change Communities need to keep their watersheds functioning. Our network or prof essionals have decades of experience understand..</p>
</div>
<div class="abs project" style="left:877px;top:1424px">
  <div class="icon"><svg width="44" height="44" viewBox="0 0 44 44" fill="none" stroke="#1d2b3a" stroke-width="1.6"><path d="M14 40V24c-6-2-8-8-8-14 4 2 8 6 8 10 0-6 2-10 6-14 2 6 0 12-6 18"/><path d="M28 14v10a4 4 0 008 0V14M30 8v6M34 8v6M32 28v12"/></svg></div>
  <h3>Energy and Food</h3><p>Security of community food and energy have, and always will be, an essential component of how communities sustain themselves. Beyond the the ecolog.</p>
</div>
<div class="abs" style="left:77px;top:1776px;width:1046px;height:1px;background:#e9ece6"></div>

<!-- recent works -->
<h2 class="abs section-title serif" style="left:0;top:1826px;font-weight:400;color:var(--blue)">Recent Works</h2>
<div class="abs work-photo" role="img" aria-label="Rows of solar panels across green farmland under a low setting sun"></div>
<div class="abs work-tag"><h3>Energy</h3><p>investment in clean energy</p></div>
<div class="abs arrows">
  <span><svg width="26" height="12" viewBox="0 0 26 12" fill="none" stroke="#a2c83e" stroke-width="1.5"><path d="M26 6H2M7 1L2 6l5 5"/></svg></span>
  <span><svg width="26" height="12" viewBox="0 0 26 12" fill="none" stroke="#a2c83e" stroke-width="1.5"><path d="M0 6h24M19 1l5 5-5 5"/></svg></span>
</div>

<!-- think green -->
<div class="abs green-bg" role="img" aria-label="Faint pale silhouettes of trees on a light background"></div>
<h2 class="abs h-blue serif" style="left:77px;top:2762px;font-weight:400;line-height:48px">Think Green !<br>Save Money</h2>
<p class="abs para" style="left:82px;top:2870px;width:380px;font-size:14.5px;line-height:25px">We are hyper focused on IMPLEMENTATION. We are eager to get about the business of preparing communities in the Pacific Northwest for fundamental change brought on by shifts in our climate and ecology.</p>
<div class="abs btn" style="left:77px;top:3032px;width:187px;background:var(--blue)">JOIN US TODAY</div>
<div class="abs btn" style="left:273px;top:3032px;width:187px;background:var(--green)">CONTACT NOW</div>
<div class="abs tree-photo" role="img" aria-label="Lone tree split between stormy cracked dry earth and sunny green meadow"></div>
<div class="abs metric" style="left:767px;top:2633px">
  <svg width="48" height="48" viewBox="0 0 48 48" fill="none" stroke="#1d2b3a" stroke-width="1.8"><circle cx="24" cy="24" r="20"/><path d="M24 24V6M24 24l15 9M24 24L9 33"/><circle cx="24" cy="24" r="3" fill="#0e8fcf"/></svg>
  <b>84%</b><span>Alternative</span></div>
<div class="abs metric" style="left:560px;top:2833px">
  <svg width="48" height="48" viewBox="0 0 48 48" fill="none" stroke="#1d2b3a" stroke-width="1.8"><path d="M24 6c8 12 12 18 12 24a12 12 0 01-24 0c0-6 4-12 12-24z" fill="#0e8fcf"/><path d="M6 40c6 4 30 4 36 0"/></svg>
  <b>98%</b><span>Clean Water</span></div>
<div class="abs metric" style="left:977px;top:2833px">
  <svg width="48" height="48" viewBox="0 0 48 48" fill="none" stroke="#1d2b3a" stroke-width="1.8"><circle cx="24" cy="18" r="12"/><circle cx="24" cy="18" r="5" fill="#0e8fcf"/><path d="M16 28l-6 14 8-3 4 6 2-12M32 28l6 14-8-3-4 6"/></svg>
  <b>56%</b><span>Forest Rescue</span></div>
<div class="abs metric" style="left:767px;top:3048px">
  <svg width="48" height="48" viewBox="0 0 48 48" fill="none" stroke="#1d2b3a" stroke-width="1.8"><path d="M24 44V6"/><path d="M24 14c-6 0-8-4-8-8 6 0 8 4 8 8zM24 14c6 0 8-4 8-8-6 0-8 4-8 8zM24 24c-6 0-8-4-8-8 6 0 8 4 8 8zM24 24c6 0 8-4 8-8-6 0-8 4-8 8zM24 34c-6 0-8-4-8-8 6 0 8 4 8 8zM24 34c6 0 8-4 8-8-6 0-8 4-8 8z" fill="#0e8fcf"/></svg>
  <b>77%</b><span>Agriculture</span></div>

<!-- contact -->
<div class="abs contact-bg" role="img" aria-label="Dark-toned rows of solar panels in a field"></div>
<h2 class="abs h-blue serif" style="left:110px;top:3325px;font-weight:400;font-size:40px">Contact Us</h2>
<p class="abs" style="left:114px;top:3382px;color:#e8ecef;font-size:14px">If you have an any Question for Contact Us Today !</p>
<div class="abs contact-line" style="left:114px;top:3420px"><svg width="18" height="24" viewBox="0 0 18 24"><path d="M9 0a9 9 0 019 9c0 6-9 15-9 15S0 15 0 9a9 9 0 019-9z" fill="#a2c83e"/><circle cx="9" cy="9" r="3.5" fill="#1d2b3a"/></svg><span>418 Alder Row,<br>Fernbrook WA<br>98000</span></div>
<div class="abs contact-line" style="left:114px;top:3520px"><svg width="20" height="20" viewBox="0 0 24 24"><path d="M6.6 10.8a15 15 0 006.6 6.6l2.2-2.2a1 1 0 011-.25 11.4 11.4 0 003.6.57 1 1 0 011 1V20a1 1 0 01-1 1A17 17 0 013 4a1 1 0 011-1h3.5a1 1 0 011 1c0 1.25.2 2.45.57 3.57a1 1 0 01-.25 1z" fill="#a2c83e"/></svg><span>555-017-3862</span></div>
<div class="abs contact-line" style="left:114px;top:3562px"><svg width="20" height="16" viewBox="0 0 20 16"><rect width="20" height="16" rx="2" fill="#a2c83e"/><path d="M1 2l9 7 9-7" fill="none" stroke="#1d2b3a" stroke-width="1.5"/></svg><span>info@cedarlinecoalition.org</span></div>
<div class="abs field" style="left:564px;top:3330px;width:251px;height:56px">Name *</div>
<div class="abs field" style="left:825px;top:3330px;width:250px;height:56px">Email *</div>
<div class="abs field" style="left:564px;top:3397px;width:251px;height:56px">Phone *</div>
<div class="abs field" style="left:825px;top:3397px;width:250px;height:56px">Services *</div>
<div class="abs field" style="left:564px;top:3463px;width:511px;height:115px">Message *</div>
<div class="abs btn" style="left:743px;top:3590px;width:146px;background:var(--green)">SUBMIT</div>

<!-- footer -->
<div class="abs footer"></div>
<div class="abs brand" style="left:70px;top:3772px;width:150px;color:var(--white);font-size:26px">Cedarline<small style="color:var(--white)">COALITION</small></div>
<div class="abs social" style="left:888px;top:3770px;gap:14px"><span class="s1" style="width:36px;height:36px"></span><span class="s2" style="width:36px;height:36px"></span><span class="s3" style="width:36px;height:36px"></span><span class="s4" style="width:36px;height:36px"></span><span class="s5" style="width:36px;height:36px"></span></div>
<div class="abs foot-links" style="left:670px;top:3826px;width:452px;text-align:right">About Us &nbsp;|&nbsp; Causes &nbsp;|&nbsp; Testimonial &nbsp;|&nbsp; Events &nbsp;|&nbsp; Contact Us</div>
<div class="abs foot-links" style="left:700px;top:3852px;width:422px;text-align:right;font-size:14px">©CEDARLINE COALITION - 2020 All rights reserved.</div>

</body>
</html>
```